Landcape Construction Company needs a flyer to catch attention

A flyer that can be displayed at several different stores detailing our skills, work produced, experience and contact details. Information can be extracted from our website www.brvkw.co.nz. The flyer should feel very green, with addition of pics of work completed as well as stock images of lush green plants, lawns, landscape or similar. Needs to be eye catching with just enough information to express our experience and commitment to high standards

Target Market(s)

Residential
Landscape Architects

Industry/Entity Type

Landscaping

Font styles to use
Serif

Colors
abd037

Requirements
Must have
• Our logo
Experience
Services offered including pictures
All information avail on our website www.brvkw.co.nz
Nice to have
• stock images of lush greenery like a garden after fresh rainfall
Should not have
• Nothing comes to mind

```html
<!DOCTYPE html>
<html lang="en">
<head>
<meta charset="utf-8">
<title>Greenline Build Company – Flyer</title>
<link href="https://fonts.googleapis.com/css2?family=Montserrat:wght@500;600;700;800&family=Libre+Baskerville:wght@400&display=swap" rel="stylesheet">
<style>
  :root{
    --page:#f1f1f1;
    --lime:#abd037;
    --leaf:#8cc63f;
    --forest:#0f6b35;
    --orange:#f0a032;
    --white:#ffffff;
  }
  *{box-sizing:border-box;margin:0;padding:0}
  html,body{width:1200px;height:900px;overflow:hidden;background:var(--page)}
  .canvas{position:relative;width:1200px;height:900px}
  .flyer{position:absolute;top:40px;width:390px;height:820px;overflow:hidden;
    box-shadow:0 10px 30px rgba(0,0,0,.18)}
  .flyer--back{left:180px}
  .flyer--front{left:630px}
  .flyer__art{position:absolute;inset:0;width:390px;height:820px}
  .serif{font-family:"Libre Baskerville",Georgia,serif}

  /* back */
  .services-pill{position:absolute;left:40px;top:404px;width:310px;height:44px;border:1.5px solid var(--white);
    border-radius:22px;display:flex;align-items:center;justify-content:center;color:var(--white);
    font-size:22px;letter-spacing:10px;padding-left:10px}
  .service-list{position:absolute;list-style:none;color:var(--white);font-size:16px;line-height:30px}
  .service-list--left{left:34px;top:468px}
  .service-list--right{left:208px;top:468px}
  .service-list li{display:flex;align-items:center;gap:8px;white-space:nowrap}
  .bullet{width:13px;height:13px;flex:none}
  .contact-list{position:absolute;list-style:none;color:var(--white);font-size:14px;line-height:22px}
  .contact-list--back{left:150px;top:752px}
  .contact-list li{display:flex;align-items:center;gap:8px}
  .contact-icon{width:13px;height:13px;flex:none}

  /* front */
  .brand{position:absolute;left:26px;top:56px;display:flex;align-items:center;gap:12px}
  .brand__mark{width:46px;height:46px;border-radius:50%;background:var(--forest);flex:none}
  .brand__name{font-family:"Montserrat",Arial,sans-serif;font-weight:600;font-size:17px;line-height:20px;color:var(--white)}
  .badge{position:absolute;left:200px;top:160px;width:110px;text-align:center;color:var(--white);font-family:"Montserrat",Arial,sans-serif}
  .badge__num{font-weight:800;font-size:44px;line-height:44px;margin-top:22px}
  .badge__label{font-weight:700;font-size:12px;letter-spacing:1px}
  .badge__ribbon{position:absolute;left:-14px;top:94px;width:138px;height:24px;background:var(--orange);
    font-weight:700;font-size:12px;letter-spacing:1px;line-height:24px;color:var(--white)}
  .headline{position:absolute;left:32px;top:372px;color:var(--white)}
  .headline__main{font-family:"Montserrat",Arial,sans-serif;font-weight:800;font-size:40px;letter-spacing:2px;line-height:44px}
  .headline__sub{font-family:"Montserrat",Arial,sans-serif;font-weight:600;font-size:15px;letter-spacing:.5px}
  .headline__rule{width:16px;height:3px;background:var(--white);margin-top:10px}
  .service-list--front{left:32px;top:466px;font-size:17px;line-height:31px}
  .contact-row{position:absolute;left:30px;bottom:24px;display:flex;gap:22px;color:var(--white);
    font-family:"Montserrat",Arial,sans-serif;font-weight:500;font-size:18px}
  .contact-row span{display:flex;align-items:center;gap:7px}
  .contact-row .contact-icon{width:16px;height:16px}
</style>
</head>
<body>
<main class="canvas">

  <!-- BACK SIDE: services -->
  <section class="flyer flyer--back">
    <svg class="flyer__art" viewBox="0 0 390 820">
      <defs>
        <linearGradient id="bgBack" x1="0" y1="0" x2="1" y2="1">
          <stop offset="0" stop-color="#9fd043"/><stop offset="1" stop-color="#88c23a"/>
        </linearGradient>
        <linearGradient id="photoBuilding" x1="0" y1="0" x2="1" y2="1">
          <stop offset="0" stop-color="#5b6066"/><stop offset=".55" stop-color="#9ea5a8"/><stop offset="1" stop-color="#6f8f52"/>
        </linearGradient>
        <linearGradient id="photoPatio" x1="0" y1="0" x2="1" y2="1">
          <stop offset="0" stop-color="#7a8e96"/><stop offset="1" stop-color="#5f7f4c"/>
        </linearGradient>
        <linearGradient id="photoDeck" x1="0" y1="0" x2="1" y2="1">
          <stop offset="0" stop-color="#8a9aa3"/><stop offset=".5" stop-color="#9c5c2c"/><stop offset="1" stop-color="#6d3c1c"/>
        </linearGradient>
        <linearGradient id="photoPaving" x1="0" y1="0" x2="1" y2="1">
          <stop offset="0" stop-color="#a8b4bc"/><stop offset="1" stop-color="#6b7378"/>
        </linearGradient>
      </defs>
      <rect width="390" height="820" fill="url(#bgBack)"/>
      <path role="img" aria-label="Photo of a modern house entrance with a louvred pergola, paved steps and hedging"
            d="M0 0H390V250C360 300 300 330 230 330C170 330 130 330 0 330Z" fill="url(#photoBuilding)"/>
      <circle role="img" aria-label="Photo of a tiled patio with garden beds" cx="95" cy="330" r="66" fill="url(#photoPatio)" stroke="#fff" stroke-width="2"/>
      <path d="M0 820V776C60 746 100 736 160 736C230 736 280 718 390 692V820Z" fill="var(--orange)"/>
      <path d="M0 820V786C60 756 104 746 164 746C234 746 284 730 390 704V820Z" fill="var(--forest)"/>
      <circle cx="108" cy="722" r="18" fill="#fff" opacity=".35"/>
      <circle role="img" aria-label="Photo of a hardwood timber deck" cx="320" cy="654" r="60" fill="url(#photoDeck)" stroke="#fff" stroke-width="2"/>
      <circle role="img" aria-label="Photo of a paved courtyard overlooking the water" cx="212" cy="688" r="54" fill="url(#photoPaving)" stroke="#fff" stroke-width="2"/>
    </svg>

    <div class="services-pill serif">SERVICES</div>

    <ul class="service-list service-list--left serif">
      <li><svg class="bullet" viewBox="0 0 14 14"><circle cx="7" cy="7" r="6" fill="none" stroke="#fff" stroke-width="1.2"/><path d="M4 7.2l2 2 4-4.4" fill="none" stroke="#fff" stroke-width="1.4"/></svg>Patios</li>
      <li><svg class="bullet" viewBox="0 0 14 14"><circle cx="7" cy="7" r="6" fill="none" stroke="#fff" stroke-width="1.2"/><path d="M4 7.2l2 2 4-4.4" fill="none" stroke="#fff" stroke-width="1.4"/></svg>Paving</li>
      <li><svg class="bullet" viewBox="0 0 14 14"><circle cx="7" cy="7" r="6" fill="none" stroke="#fff" stroke-width="1.2"/><path d="M4 7.2l2 2 4-4.4" fill="none" stroke="#fff" stroke-width="1.4"/></svg>Concrete</li>
      <li><svg class="bullet" viewBox="0 0 14 14"><circle cx="7" cy="7" r="6" fill="none" stroke="#fff" stroke-width="1.2"/><path d="M4 7.2l2 2 4-4.4" fill="none" stroke="#fff" stroke-width="1.4"/></svg>Water Features</li>
      <li><svg class="bullet" viewBox="0 0 14 14"><circle cx="7" cy="7" r="6" fill="none" stroke="#fff" stroke-width="1.2"/><path d="M4 7.2l2 2 4-4.4" fill="none" stroke="#fff" stroke-width="1.4"/></svg>Decking</li>
    </ul>
    <ul class="service-list service-list--right serif">
      <li><svg class="bullet" viewBox="0 0 14 14"><circle cx="7" cy="7" r="6" fill="none" stroke="#fff" stroke-width="1.2"/><path d="M4 7.2l2 2 4-4.4" fill="none" stroke="#fff" stroke-width="1.4"/></svg>Fencing</li>
      <li><svg class="bullet" viewBox="0 0 14 14"><circle cx="7" cy="7" r="6" fill="none" stroke="#fff" stroke-width="1.2"/><path d="M4 7.2l2 2 4-4.4" fill="none" stroke="#fff" stroke-width="1.4"/></svg>Boardwalks</li>
      <li><svg class="bullet" viewBox="0 0 14 14"><circle cx="7" cy="7" r="6" fill="none" stroke="#fff" stroke-width="1.2"/><path d="M4 7.2l2 2 4-4.4" fill="none" stroke="#fff" stroke-width="1.4"/></svg>Timber</li>
      <li><svg class="bullet" viewBox="0 0 14 14"><circle cx="7" cy="7" r="6" fill="none" stroke="#fff" stroke-width="1.2"/><path d="M4 7.2l2 2 4-4.4" fill="none" stroke="#fff" stroke-width="1.4"/></svg>Planter Boxes</li>
    </ul>

    <ul class="contact-list contact-list--back serif">
      <li><svg class="contact-icon" viewBox="0 0 14 14"><rect x="1" y="3" width="12" height="8" fill="none" stroke="var(--orange)" stroke-width="1.3"/><path d="M1 3l6 5 6-5" fill="none" stroke="var(--orange)" stroke-width="1.3"/></svg>mark@brvkw.co.nz</li>
      <li><svg class="contact-icon" viewBox="0 0 14 14"><circle cx="7" cy="7" r="6" fill="none" stroke="var(--orange)" stroke-width="1.3"/><path d="M5 4.2c-.8.6-.6 2.2.6 3.6s2.8 2 3.6 1.4l-1-1.2-.9.4c-.6-.3-1.2-1-1.5-1.6l.5-.9z" fill="var(--orange)"/></svg>021 555 014</li>
      <li><svg class="contact-icon" viewBox="0 0 14 14"><circle cx="7" cy="7" r="6" fill="none" stroke="var(--orange)" stroke-width="1.3"/><ellipse cx="7" cy="7" rx="2.6" ry="6" fill="none" stroke="var(--orange)" stroke-width="1"/><path d="M1 7h12" stroke="var(--orange)" stroke-width="1"/></svg>www.brvkw.co.nz</li>
    </ul>
  </section>

  <!-- FRONT SIDE -->
  <section class="flyer flyer--front">
    <svg class="flyer__art" viewBox="0 0 390 820">
      <defs>
        <linearGradient id="bgFront" x1="0" y1="0" x2="1" y2="1">
          <stop offset="0" stop-color="#9fd043"/><stop offset="1" stop-color="#abd037"/>
        </linearGradient>
        <linearGradient id="photoGarden" x1="0" y1="0" x2="1" y2="1">
          <stop offset="0" stop-color="#3f8a2a"/><stop offset=".45" stop-color="#54b636"/><stop offset=".8" stop-color="#3e9a2c"/><stop offset="1" stop-color="#9c4a5a"/>
        </linearGradient>
        <linearGradient id="photoWall" x1="0" y1="0" x2="1" y2="1">
          <stop offset="0" stop-color="#4f7f32"/><stop offset="1" stop-color="#8e8a7c"/>
        </linearGradient>
        <linearGradient id="photoSprinkler" x1="0" y1="0" x2="1" y2="1">
          <stop offset="0" stop-color="#b8c9a4"/><stop offset="1" stop-color="#4fa53a"/>
        </linearGradient>
      </defs>
      <rect width="390" height="820" fill="url(#bgFront)"/>
      <path role="img" aria-label="Photo of a lush green lawn edged with clipped hedges and flowering shrubs"
            d="M0 300C120 250 240 240 300 170C330 140 370 120 390 110V640H0Z" fill="url(#photoGarden)"/>
      <path d="M0 292C110 240 230 236 300 164C330 132 365 116 390 104V116C366 130 334 148 306 178C236 252 118 262 0 306Z" fill="var(--orange)"/>
      <path d="M0 306C118 262 236 252 306 178C334 148 366 130 390 116V124C366 140 338 160 312 188C240 264 120 276 0 316Z" fill="var(--white)"/>
      <circle cx="255" cy="212" r="56" fill="var(--white)"/>
      <circle cx="255" cy="212" r="50" fill="var(--forest)"/>
      <path d="M0 640C80 650 150 640 210 640C280 640 350 620 390 580V820H0Z" fill="var(--orange)"/>
      <path d="M0 680C80 690 150 670 220 660C290 650 350 630 390 600V820H0Z" fill="var(--forest)"/>
      <path d="M0 676C80 686 150 666 220 656" fill="none" stroke="#fff" stroke-width="2"/>
      <circle role="img" aria-label="Photo of a natural stone retaining wall with hedging" cx="125" cy="700" r="68" fill="url(#photoWall)" stroke="#fff" stroke-width="2"/>
      <circle role="img" aria-label="Photo of a lawn sprinkler watering green grass" cx="258" cy="664" r="60" fill="url(#photoSprinkler)" stroke="#fff" stroke-width="2"/>
    </svg>

    <div class="brand">
      <div class="brand__mark"></div>
      <div class="brand__name">The Greenline Build<br>Company Ltd</div>
    </div>

    <div class="badge">
      <div class="badge__num">25</div>
      <div class="badge__label">YEARS</div>
      <div class="badge__ribbon">EXPERIENCE</div>
    </div>

    <div class="headline">
      <div class="headline__main">LOCALLY</div>
      <div class="headline__sub">OWNED AND OPERATED</div>
      <div class="headline__rule"></div>
    </div>

    <ul class="service-list service-list--front serif">
      <li><svg class="bullet" viewBox="0 0 14 14"><circle cx="7" cy="7" r="6" fill="none" stroke="#fff" stroke-width="1.2"/><path d="M4 7.2l2 2 4-4.4" fill="none" stroke="#fff" stroke-width="1.4"/></svg>Retaining Walls</li>
      <li><svg class="bullet" viewBox="0 0 14 14"><circle cx="7" cy="7" r="6" fill="none" stroke="#fff" stroke-width="1.2"/><path d="M4 7.2l2 2 4-4.4" fill="none" stroke="#fff" stroke-width="1.4"/></svg>Gardens &amp; Lawns</li>
      <li><svg class="bullet" viewBox="0 0 14 14"><circle cx="7" cy="7" r="6" fill="none" stroke="#fff" stroke-width="1.2"/><path d="M4 7.2l2 2 4-4.4" fill="none" stroke="#fff" stroke-width="1.4"/></svg>Irrigation</li>
      <li><svg class="bullet" viewBox="0 0 14 14"><circle cx="7" cy="7" r="6" fill="none" stroke="#fff" stroke-width="1.2"/><path d="M4 7.2l2 2 4-4.4" fill="none" stroke="#fff" stroke-width="1.4"/></svg>Project Management</li>
      <li><svg class="bullet" viewBox="0 0 14 14"><circle cx="7" cy="7" r="6" fill="none" stroke="#fff" stroke-width="1.2"/><path d="M4 7.2l2 2 4-4.4" fill="none" stroke="#fff" stroke-width="1.4"/></svg>Consultation</li>
    </ul>

    <div class="contact-row">
      <span><svg class="contact-icon" viewBox="0 0 14 14"><circle cx="7" cy="7" r="6" fill="none" stroke="var(--orange)" stroke-width="1.3"/><path d="M5 4.2c-.8.6-.6 2.2.6 3.6s2.8 2 3.6 1.4l-1-1.2-.9.4c-.6-.3-1.2-1-1.5-1.6l.5-.9z" fill="var(--orange)"/></svg>021 555 014</span>
      <span><svg class="contact-icon" viewBox="0 0 14 14"><circle cx="7" cy="7" r="6" fill="none" stroke="var(--orange)" stroke-width="1.3"/><ellipse cx="7" cy="7" rx="2.6" ry="6" fill="none" stroke="var(--orange)" stroke-width="1"/><path d="M1 7h12" stroke="var(--orange)" stroke-width="1"/></svg>www.brvkw.co.nz</span>
    </div>
  </section>

</main>
</body>
</html>
```